This project is a poster that will be in the public/lobby areas of ice hockey rinks to introduce an initiative to address the rampant abuse of officials.

Communication Objectives:
- Capture Attention
- Awareness of New Initiative
- Create Curiosity to Learn More
- Build Recognition of BTP?!? (Name/Branding/Mission)
- Target Audience is Hockey Players, Coaches, Parents, Officials
- Work together to create solutions ... not point fingers or assign blame.

This poster is most likely going to be 11"x17" and/or 16"x20"

Primary Message:
1) IT’S NOT OK!!!
Ice hockey has experienced a significant increase in unacceptable behavior by players, coaches, parents, fans, and officials. It’s time for an intervention that will bring an end to the adversarial environment in the rink that has been negatively impacting all of us. The way things are right now in this sport IS NOT OK!!!

2) WE CAN ALL DO BETTER
Nobody wins when on-ice officials are abused by coaches, players, parents, or fans. This type of behavior is not only inexcusable, but also completely unproductive.
Abusive behavior does not change anything that has already occurred, and it certainly isn’t going to change future calls to the abuser’s advantage.
Whistles don’t get unblown, disputed calls/non-calls don’t get overturned, and penalties don’t get dismissed.
Instead, emotions take control, tempers flare, more penalties ensue, inappropriate behavior escalates, and ultimately the safety of all participants is placed at risk.
This behavior merely creates an adversarial and combative environment that will always negatively impact the remainder of the game for everyone involved.

3) What is BEYOND THE PLAY?!?
We are referees who are partnering with players, coaches, parents, and fans to address and eliminate unacceptable behavior. We are developing tools to facilitate an alignment between on-ice officials and those for whom we officiate. We aren’t interested in complaining or assigning blame, but genuinely want to find solutions that ALL of us can accept, and will be willing to implement, and stand behind.

BeyondThePlay?!? Branding Images & Logo should be prominently displayed within the design.

Target Market(s)

Ice hockey players, coaches, parents, and fans. Poster will be in the public lobby area of ice hockey rinks throughout Northeastern United States.

Industry/Entity Type

Youth Sports & Activities

Colors

Designer to choose colors to be used in the design.

Requirements
Must have
• Branding elements for BeyondThePlay?!? including logo, BTP?!? icon, IT'S NOT OK!!! tagline & We Can All Do Better tagline
Nice to have
• I've included some body text as part of the project brief.

```html
<!DOCTYPE html>
<html lang="en">
<head>
<meta charset="utf-8">
<title>It's Not OK!!! – Beyond The Play?!?</title>
<link href="https://fonts.googleapis.com/css2?family=Open+Sans:ital,wght@1,700&family=Roboto+Condensed:wght@300;700&display=swap" rel="stylesheet">
<style>
  :root {
    --ink: #1d1d1b;
    --brand-blue: #0a6db3;
    --deep-blue: #1a5690;
    --light-blue: #9fc2e4;
    --orange: #f0862f;
    --body: #333;
    --white: #fff;
  }
  html, body { margin: 0; padding: 0; overflow: hidden; }
  body { width: 776px; height: 1200px; background: var(--white); }
  .poster { position: relative; width: 776px; height: 1200px; overflow: hidden; background: var(--white); font-family: 'Roboto Condensed', sans-serif; }

  .title-bar { position: absolute; left: 0; top: 59px; width: 43px; height: 82px; background: linear-gradient(90deg, var(--brand-blue), #1379c0); }
  .headline { position: absolute; left: 64px; top: 36px; margin: 0; font: 700 123px/1 'Roboto Condensed', sans-serif; color: var(--ink); letter-spacing: -1px; white-space: nowrap; }

  .action-photo { position: absolute; left: 372px; top: 160px; width: 404px; height: 580px;
    background: linear-gradient(160deg, #e6e6ee 0%, #9a9aae 35%, #6d6d82 55%, #c5c8d6 75%, #ffffff 100%);
    clip-path: polygon(88px 0, 404px 0, 404px 420px, 385px 580px, 250px 575px, 90px 460px, 70px 400px, 20px 390px, 18px 300px, 60px 240px, 115px 80px);
  }

  .intro { position: absolute; left: 41px; top: 170px; width: 340px; margin: 0; font: italic 700 21.5px/27.5px 'Open Sans', sans-serif; color: var(--deep-blue); white-space: nowrap; }
  .intro .marker { display: inline-block; width: 14px; height: 14px; background: var(--orange); margin-right: 11px; vertical-align: 2px; }

  .banner { position: absolute; display: flex; align-items: center; }
  .banner .tab { width: 20px; height: 100%; background: var(--orange); flex: none; }
  .banner .field { height: 100%; flex: 1; background: linear-gradient(90deg, var(--brand-blue), var(--light-blue)); clip-path: polygon(0 0, 92% 0, 100% 100%, 0 100%); display: flex; align-items: center; }
  .banner h2 { margin: 0; color: var(--white); font: 700 36px/36px 'Roboto Condensed', sans-serif; text-shadow: 2px 2px 3px rgba(0,0,0,.45); }
  .banner-better { left: 35px; top: 557px; width: 359px; height: 88px; }
  .banner-better h2 { padding-left: 17px; }
  .banner-what { left: 206px; top: 941px; width: 504px; height: 50px; }
  .banner-what h2 { padding-left: 15px; font-size: 34px; }

  .side-wash { position: absolute; left: 0; top: 790px; width: 60px; height: 100px; background: linear-gradient(90deg, #d7e6f3, rgba(255,255,255,0)); }

  .copy { position: absolute; margin: 0; font: 300 16.3px/21px 'Roboto Condensed', sans-serif; color: var(--body); white-space: nowrap; }
  .copy-1 { left: 35px; top: 668px; }
  .copy-2 { left: 33px; top: 737px; }
  .copy-3 { left: 33px; top: 788px; }
  .copy-4 { left: 209px; top: 862px; }
  .copy-5 { left: 209px; top: 1009px; }

  .brand-lockup { position: absolute; left: 40px; top: 980px; width: 150px; display: flex; align-items: center; gap: 8px; }
  .brand-lockup .brand-dot { width: 14px; height: 14px; border-radius: 50%; background: var(--orange); flex: none; }
  .brand-lockup .brand-name { font: 700 17px/1.2 'Roboto Condensed', sans-serif; color: var(--ink); }

  .footer-band { position: absolute; left: 0; top: 1150px; width: 776px; height: 50px; background: linear-gradient(90deg, var(--brand-blue) 0%, #5aa6d6 45%, #b9d9ee 80%, #ffffff 100%); }
</style>
</head>
<body>
<main class="poster">
  <div class="title-bar"></div>
  <h1 class="headline">IT’S NOT OK!!!</h1>

  <div class="action-photo" role="img" aria-label="Photo of a hockey face-off with a referee dropping the puck, a coach arguing with an official in the background"></div>

  <p class="intro"><span class="marker"></span>Ice hockey has experienced<br>a significant increase in<br>unacceptable behavior by<br>players, coaches, parents, fans,<br>and officials. It’s time for an<br>intervention that will bring<br>an end to the adversarial<br>environment in the rink<br>that has been negatively<br>impacting all of us. The<br>way things are right<br>now in this sport<br>IS NOT OK!!!</p>

  <div class="banner banner-better">
    <div class="tab"></div>
    <div class="field"><h2>WE CAN ALL DO<br>BETTER</h2></div>
  </div>

  <div class="side-wash"></div>

  <p class="copy copy-1">Nobody wins when on-ice officials are abused by coaches, players, parents, or<br>fans. This type of behavior is not only inexcusable, but also completely unpro-<br>ductive.</p>
  <p class="copy copy-2">Abusive behavior does not change anything that has already occurred, and it certainly isn’t going to change<br>future calls to the abuser’s advantage.</p>
  <p class="copy copy-3">Whistles don’t get unblown, disputed calls/non-calls don’t get overturned, and penalties don’t get dismissed.<br>Instead, emotions take control, tempers flare, more penalties ensue, inappropriate behavior escalates, and ulti-<br>mately the safety of all participants is placed at risk.</p>
  <p class="copy copy-4">This behavior merely creates an adversarial and combative environment that will<br>always negatively impact the remainder of the game for everyone involved.</p>

  <div class="brand-lockup">
    <span class="brand-dot"></span>
    <span class="brand-name">BEYOND THE PLAY?!?</span>
  </div>

  <div class="banner banner-what">
    <div class="tab"></div>
    <div class="field"><h2>What is BEYOND THE PLAY?!?</h2></div>
  </div>

  <p class="copy copy-5">We are referees who are partnering with players, coaches, parents, and fans to ad-<br>dress and eliminate unacceptable behavior. We are developing tools to facilitate an<br>alignment between on-ice officials and those for whom we officiate. We aren’t inte-<br>rested in complaining or assigning blame, but genuinely want to find solutions that<br>ALL of us can accept, and will be willing to implement, and stand behind.</p>

  <div class="footer-band"></div>
</main>
</body>
</html>
```